Tech + Media Consulting Business // LOGO + Card

We need a logo design and business card for a Seattle-area strategy consulting firm. We believe in big, expansive thinking and we work for tech/media startups, as well as big companies like Quorvane and Tunelark. We would like designs inspired by the mountains and skies of Montana and Colorado. Existing logo attached but we would like a fresh approach.

Target Market(s)

Technology and Media Executives

Industry/Entity Type

Information Technology

Contact Information for Business Card

Marcus Lindholt
2157 61st Avenue NE
Medina WA 98027
Phone: 206-471-2958
marcuslindholt@ridgeframeadvisory.biz

Logo Text

Ridgeframe Advisory LLC

Font styles to use
Sans Serif

Colors

Designer to choose colors to be used in the design.

Requirements
Must have
• Logo inspired by mountains and sky.
• Our company wants to inspire our clients to think expansively -- embracing exploration and new ideas.
Nice to have
• Colors inspired by Fernwald-brand.
• We don't have a website at present but would like a field to add one later. Until then, we may reference our LinkedIn page:
• https://www.linkedin.com/company/ridgeframe-advisory-llc-nw

```html
<!DOCTYPE html>
<html lang="en">
<head>
<meta charset="utf-8">
<title>Ridgeframe Advisory LLC — Business Card</title>
<link rel="stylesheet" href="https://fonts.googleapis.com/css2?family=Lato:wght@400;700&family=Michroma&display=swap">
<style>
  :root {
    --backdrop: #efe9e1;
    --kraft-light: #dcb98d;
    --kraft-mid: #cfa575;
    --kraft-dark: #c39463;
    --ink: #141010;
  }
  * { margin: 0; padding: 0; box-sizing: border-box; }
  html, body {
    width: 1200px;
    height: 900px;
    overflow: hidden;
    background: var(--backdrop);
  }
  .canvas {
    position: relative;
    width: 1200px;
    height: 900px;
  }
  .card {
    position: absolute;
    left: 330px;
    width: 556px;
    height: 343px;
    background: linear-gradient(160deg, var(--kraft-light) 0%, var(--kraft-mid) 55%, var(--kraft-dark) 100%);
    color: var(--ink);
    font-family: "Lato", sans-serif;
    text-align: center;
  }
  .card--front { top: 90px; }
  .card--back { top: 470px; }

  .contact {
    position: absolute;
    left: 0;
    right: 0;
    top: 84px;
    display: flex;
    flex-direction: column;
    align-items: center;
  }
  .contact__name {
    font-family: "Michroma", sans-serif;
    font-size: 17px;
    letter-spacing: 1px;
    text-transform: uppercase;
    line-height: 24px;
    font-weight: 400;
    -webkit-text-stroke: 0.5px var(--ink);
  }
  .contact__rule {
    width: 202px;
    height: 1px;
    background: var(--ink);
    border: 0;
  }
  .contact__rule--top { margin-top: 15px; }
  .contact__rule--bottom { margin-top: 14px; }
  .contact__address {
    margin-top: 21px;
    font-size: 15.5px;
    line-height: 21px;
    font-style: normal;
  }
  .contact__reach {
    margin-top: 16px;
    font-size: 15.5px;
    line-height: 20px;
  }

  .brand {
    position: absolute;
    left: 0;
    right: 0;
    top: 92px;
    display: flex;
    flex-direction: column;
    align-items: center;
  }
  .brand__mark {
    width: 76px;
    height: 76px;
    border-radius: 50%;
    background: var(--ink);
  }
  .brand__name {
    margin-top: 22px;
    font-family: "Lato", sans-serif;
    font-weight: 700;
    font-size: 32px;
    line-height: 40px;
    letter-spacing: 0.5px;
    color: var(--ink);
  }
</style>
</head>
<body>
  <main class="canvas">
    <section class="card card--front" aria-label="Business card front">
      <div class="contact">
        <h1 class="contact__name">Marcus Lindholt</h1>
        <hr class="contact__rule contact__rule--top">
        <address class="contact__address">
          2157 61st Avenue NE<br>
          Medina WA 98027
        </address>
        <hr class="contact__rule contact__rule--bottom">
        <p class="contact__reach">
          206-471-2958<br>
          marcuslindholt@ridgeframeadvisory.biz
        </p>
      </div>
    </section>

    <section class="card card--back" aria-label="Business card back">
      <div class="brand">
        <div class="brand__mark" aria-hidden="true"></div>
        <p class="brand__name">Ridgeframe Advisory LLC</p>
      </div>
    </section>
  </main>
</body>
</html>
```